Velmar Ops Business Cards

We need to design some upbeat business cards. We are an Industrial Rope Access Company/Height Safety Company that specialize in Rope Access, Confined Space, Anchor Points, Safety Systems, PPE Inspecions and Rigging.
Company name is Velmar Ops Ltd
Card is for Gareth Lomas the Company Director
His mobile number is 027 418 9072 and email is gareth@velmarops.co.nz. Website address is www.velmarops.co.nz.
We will post some pictures below to ensure you get a good idea of what we do.

```html
<!DOCTYPE html>
<html lang="en">
<head>
<meta charset="utf-8">
<title>Velmar Ops Business Cards</title>
<link href="https://fonts.googleapis.com/css2?family=Saira:wght@400;500;600;700&display=swap" rel="stylesheet">
<style>
  :root {
    --page-bg: #1b1b1c;
    --card-black: #0c0c0d;
    --gloss-text: #2a2c2d;
    --gloss-strong: #3a3d3f;
    --card-blue: #2352b8;
    --card-blue-dark: #1e47a3;
    --watermark-blue: #2a5bc6;
    --white: #ffffff;
  }
  * { margin: 0; padding: 0; box-sizing: border-box; }
  html, body { width: 1200px; height: 896px; overflow: hidden; }
  body {
    background: var(--page-bg);
    font-family: "Saira", "Arial Narrow", sans-serif;
    display: flex;
    align-items: center;
    justify-content: center;
    gap: 40px;
  }
  .card {
    position: relative;
    width: 540px;
    height: 310px;
    border-radius: 16px;
    overflow: hidden;
    box-shadow: 0 18px 40px rgba(0,0,0,0.55);
  }

  /* Front: black card with gloss lettering */
  .card-front { background: var(--card-black); }
  .brand-name {
    position: absolute;
    left: 34px;
    top: 28px;
    font-size: 74px;
    font-weight: 700;
    letter-spacing: 1px;
    line-height: 1;
    color: var(--gloss-strong);
  }
  .service-list {
    position: absolute;
    list-style: none;
    font-size: 15px;
    font-weight: 500;
    line-height: 22px;
    color: var(--gloss-text);
  }
  .service-list li { display: flex; align-items: center; gap: 8px; }
  .service-list--left { left: 34px; bottom: 22px; }
  .service-list--right { right: 30px; top: 118px; text-align: right; }
  .service-list--right li { justify-content: flex-end; }
  .tick { width: 12px; height: 12px; flex: none; }

  /* Back: blue contact card */
  .card-back {
    background: linear-gradient(160deg, var(--card-blue) 0%, var(--card-blue-dark) 100%);
    color: var(--white);
  }
  .watermark {
    position: absolute;
    left: -6px;
    top: 20px;
    font-size: 150px;
    font-weight: 700;
    line-height: 1;
    letter-spacing: 2px;
    color: var(--watermark-blue);
    white-space: nowrap;
  }
  .person {
    position: absolute;
    left: 34px;
    top: 150px;
  }
  .person-name {
    font-size: 50px;
    font-weight: 700;
    line-height: 1;
  }
  .person-role {
    font-size: 11px;
    font-weight: 500;
    letter-spacing: 3px;
    text-transform: uppercase;
    margin-top: 4px;
  }
  .contact-line {
    position: absolute;
    left: 34px;
    right: 30px;
    bottom: 22px;
    font-size: 13.5px;
    font-weight: 500;
    letter-spacing: 0.3px;
    white-space: nowrap;
  }
  .contact-line .sep { margin: 0 8px; }
</style>
</head>
<body>

<svg width="0" height="0" style="position:absolute">
  <defs>
    <symbol id="tick-box" viewBox="0 0 12 12">
      <rect x="0.75" y="2.75" width="8.5" height="8.5" fill="none" stroke="currentColor" stroke-width="1.3"/>
      <path d="M2.5 6.5 L5 9 L11 1.5" fill="none" stroke="currentColor" stroke-width="1.5"/>
    </symbol>
  </defs>
</svg>

<section class="card card-front">
  <div class="brand-name">Velmar Ops</div>

  <ul class="service-list service-list--left">
    <li><svg class="tick"><use href="#tick-box"/></svg>Rope Access</li>
    <li><svg class="tick"><use href="#tick-box"/></svg>Anchor Points</li>
    <li><svg class="tick"><use href="#tick-box"/></svg>PPE Certification</li>
    <li><svg class="tick"><use href="#tick-box"/></svg>Rope Access</li>
    <li><svg class="tick"><use href="#tick-box"/></svg>Anchor Points</li>
    <li><svg class="tick"><use href="#tick-box"/></svg>PPE Certification</li>
  </ul>

  <ul class="service-list service-list--right">
    <li>Confined Space<svg class="tick"><use href="#tick-box"/></svg></li>
    <li>Safety Systems<svg class="tick"><use href="#tick-box"/></svg></li>
    <li>Rigging<svg class="tick"><use href="#tick-box"/></svg></li>
    <li>Confined Space<svg class="tick"><use href="#tick-box"/></svg></li>
    <li>Safety Systems<svg class="tick"><use href="#tick-box"/></svg></li>
    <li>Rigging<svg class="tick"><use href="#tick-box"/></svg></li>
  </ul>
</section>

<section class="card card-back">
  <div class="watermark" aria-hidden="true">Velmar Ops</div>
  <div class="person">
    <div class="person-name">Gareth Lomas</div>
    <div class="person-role">Director</div>
  </div>
  <div class="contact-line">
    <span>027 418 9072</span><span class="sep">|</span><span>gareth@velmarops.co.nz</span><span class="sep">|</span><span>www.velmarops.co.nz</span>
  </div>
</section>

</body>
</html>
```